we are an outdoor outlet in a country club that has a variety of outlets. The Club is called Lanterns and is located in Cairo, Egypt. This garden menu will include cuisines from the Mediterranean, Asia and Texmex. we need a menu that is colorful and would fit an A3 size, back and front are to be used. Attached is the old menu currently in use (Garden Menu 2012.pdf is just for reference) and the new menu text for you to use is under the name Garden Menu Fall 2013
thank you.

```html
<!DOCTYPE html>
<html lang="en">
<head>
<meta charset="utf-8">
<title>Garden Menu – Lanterns Country Club</title>
<link href="https://fonts.googleapis.com/css2?family=PT+Sans:wght@400;700&family=PT+Serif:wght@400;700&display=swap" rel="stylesheet">
<style>
  :root {
    --paper-light: #f6e4bd;
    --paper-dark: #eecf98;
    --maroon: #7c2530;
    --rust: #c94b2a;
    --rust-dark: #a8402a;
    --orange: #f26b2e;
    --orange-deep: #e45a22;
    --ribbon-red: #cf4a26;
    --ribbon-green: #c9d46a;
    --ribbon-green-dark: #9aa63f;
    --leaf: #d8c47a;
    --logo-green: #8a8f2a;
    --ink-dark: #4a1f16;
    --white: #ffffff;
    --badge: #b5422a;
  }
  * { margin: 0; padding: 0; box-sizing: border-box; }
  html, body { width: 848px; height: 1200px; overflow: hidden; }
  body {
    position: relative;
    background: radial-gradient(ellipse at 50% 40%, var(--paper-light), var(--paper-dark));
    font-family: "PT Sans", Arial, sans-serif;
    color: var(--rust);
  }
  .frame {
    position: absolute; left: 22px; top: 30px; width: 804px; height: 1140px;
    border: 3px solid var(--white);
  }
  .title-band {
    position: absolute; left: 25px; top: 33px; width: 798px; height: 82px;
    background: rgba(255, 247, 228, 0.55);
  }
  .menu-title {
    position: absolute; left: 100px; top: 50px;
    font-weight: 700; font-size: 52px; letter-spacing: 1px; color: var(--maroon);
    line-height: 1;
  }
  .club-name {
    position: absolute; left: 570px; top: 56px; display: flex; align-items: center; gap: 8px;
  }
  .club-dot { width: 34px; height: 34px; border-radius: 50%; background: var(--logo-green); }
  .club-text { font-size: 24px; line-height: 0.9; color: var(--logo-green); font-weight: 400; }
  .club-text small { display: block; font-size: 11px; letter-spacing: 2px; }

  .ribbon { position: absolute; left: 0; top: 128px; width: 848px; height: 70px; }
  .ribbon-label {
    position: absolute; left: 236px; top: 131px; width: 400px; height: 48px;
    display: flex; align-items: center; justify-content: center;
    color: var(--white); font-size: 28px; letter-spacing: 0.5px;
  }

  .column { position: absolute; }
  .col-left { left: 100px; width: 285px; }
  .col-right { left: 459px; width: 287px; }
  .section-head {
    text-align: center; font-weight: 700; font-size: 20px; color: var(--maroon); line-height: 1;
  }
  .section-note { text-align: center; font-family: "PT Serif", Georgia, serif; font-size: 9px; color: var(--maroon); margin-top: 1px; }
  .rule { position: relative; height: 18px; margin-top: 4px; }
  .rule::before { content: ""; position: absolute; left: 0; right: 0; top: 7px; border-top: 1px solid #ddbf80; }
  .ornament { position: absolute; left: 50%; top: 1px; width: 14px; height: 14px; margin-left: -7px; background: var(--leaf); border-radius: 50%; }

  .menu-list { list-style: none; }
  .item { position: relative; }
  .item-name { font-size: 12px; text-transform: uppercase; color: var(--rust); line-height: 14px; }
  .item-desc { font-family: "PT Serif", Georgia, serif; font-size: 9px; line-height: 12px; color: var(--rust-dark); }
  .item-price { position: absolute; right: 0; top: 0; font-size: 12px; color: var(--rust); }
  .appetizers .item { height: 38.6px; }
  .soups .item { height: 50px; }
  .salads .item { height: 50px; }
  .sub-option { font-size: 9.5px; line-height: 13.5px; padding-left: 0; position: relative; }
  .sub-option .bullet { display: inline-block; width: 6px; height: 6px; border-radius: 50%; background: var(--rust); margin-right: 6px; vertical-align: 0; }
  .sub-option .item-price { font-size: 9px; }

  .mains-panel {
    position: absolute; left: 463px; top: 636px; width: 342px; height: 488px;
    background: var(--orange); border-radius: 16px;
    box-shadow: 2px 3px 5px rgba(120, 60, 20, 0.25);
  }
  .mains-inner {
    position: absolute; left: 7px; top: 7px; right: 7px; bottom: 7px;
    border: 1px dashed rgba(255, 255, 255, 0.8); border-radius: 12px;
  }
  .mains-head { position: absolute; left: 0; right: 0; top: 22px; text-align: center; font-weight: 700; font-size: 25px; color: var(--ink-dark); }
  .mains-rule { position: absolute; left: 28px; right: 28px; top: 56px; border-top: 1px solid rgba(255,255,255,0.6); }
  .mains-ornament { position: absolute; left: 164px; top: 52px; width: 12px; height: 12px; border-radius: 50%; background: #fbd2b3; }
  .mains-list { position: absolute; left: 28px; top: 74px; width: 283px; list-style: none; }
  .main-item { position: relative; }
  .main-item .item-name { font-size: 15px; line-height: 18px; color: var(--white); }
  .main-item .item-desc { font-size: 11px; line-height: 15px; color: var(--ink-dark); font-weight: 700; }
  .main-item .item-price { font-size: 15px; color: var(--white); }
  .sauce { font-family: "PT Serif", Georgia, serif; font-size: 11px; line-height: 15px; font-weight: 700; color: var(--white); }
  .sauce::before { content: ""; display: inline-block; width: 6px; height: 6px; border-radius: 50%; background: var(--white); margin-right: 5px; vertical-align: 1px; }

  .olive-art {
    position: absolute; left: 416px; top: 634px; width: 100px; height: 74px;
    background: radial-gradient(ellipse at 40% 55%, #7a5a3e, #b49a74 70%, transparent 72%);
  }
  .price-badge {
    position: absolute; left: 390px; top: 1084px; width: 98px; height: 98px; border-radius: 50%;
    background: var(--badge); display: flex; align-items: center; justify-content: center; text-align: center;
  }
  .price-badge::before { content: ""; position: absolute; inset: 5px; border: 1px dashed rgba(255,255,255,0.7); border-radius: 50%; }
  .price-badge p { font-family: "PT Serif", Georgia, serif; font-size: 7.5px; line-height: 9px; color: var(--white); width: 70px; font-weight: 700; }
</style>
</head>
<body>
  <div class="title-band"></div>
  <div class="frame"></div>

  <h1 class="menu-title">GARDEN MENU</h1>
  <div class="club-name">
    <span class="club-dot"></span>
    <span class="club-text">lanterns<small>country club</small></span>
  </div>

  <svg class="ribbon" viewBox="0 0 848 70" aria-hidden="true">
    <polygon points="100,16 258,16 258,58 120,58 138,37" fill="var(--ribbon-green)"/>
    <polygon points="590,16 800,16 782,37 800,58 590,58" fill="var(--ribbon-green)"/>
    <polygon points="236,51 258,51 258,62" fill="var(--ribbon-green-dark)"/>
    <polygon points="612,51 636,51 612,62" fill="var(--ribbon-green-dark)"/>
    <rect x="236" y="3" width="400" height="48" fill="var(--ribbon-red)"/>
  </svg>
  <div class="ribbon-label">MEDITERRANEAN CORNER</div>

  <!-- Left column -->
  <section class="column col-left appetizers" style="top:200px">
    <h2 class="section-head">appetizers</h2>
    <div class="rule"><span class="ornament" role="img" aria-label="Leaf ornament"></span></div>
    <ul class="menu-list" style="margin-top:2px">
      <li class="item"><div class="item-name">Turkish Brioche</div><div class="item-desc">Filled with seasoned chicken and basmati rice</div><span class="item-price">00</span></li>
      <li class="item"><div class="item-name">Roasted Eggplant Rolls</div><div class="item-desc">With herbed ricotta cheese and pine nuts</div><span class="item-price">00</span></li>
      <li class="item"><div class="item-name">Falafel in Mini Pita</div><div class="item-desc">Served with tehina and oriental salsa</div><span class="item-price">00</span></li>
      <li class="item"><div class="item-name">Mankousha</div><div class="item-desc">With thyme and olive oil</div><span class="item-price">00</span></li>
      <li class="item"><div class="item-name">Fried Kobeba</div><div class="item-desc">With minced meat, spices, and pine nuts</div><span class="item-price">00</span></li>
      <li class="item"><div class="item-name">Fried Calamari a la Romana</div><div class="item-desc">Served with aioli</div><span class="item-price">00</span></li>
      <li class="item"><div class="item-name">Samboussek</div><div class="item-desc">With herbed white cheese and mint</div><span class="item-price">00</span></li>
      <li class="item"><div class="item-name">Oriental Sausage</div><div class="item-desc">Sautéed with garlic and onion</div><span class="item-price">00</span></li>
      <li class="item"><div class="item-name">Mini Vine Leaves</div><div class="item-desc">With a yoghurt dip</div><span class="item-price">00</span></li>
      <li class="item"><div class="item-name">Fatouch</div><div class="item-desc">With a pomegranate syrup dressing</div><span class="item-price">00</span></li>
      <li class="item"><div class="item-name">Hummus</div><div class="item-desc">Seasoned with lemon juice, garlic, and olive oil</div><span class="item-price">00</span></li>
      <li class="item"><div class="item-name">White Cheese</div><div class="item-desc">With diced tomato, thyme, and olive oil</div><span class="item-price">00</span></li>
      <li class="item"><div class="item-name">Tehina</div><div class="item-desc">Seasoned with cumin, lemon juice, and garlic</div><span class="item-price">00</span></li>
    </ul>
  </section>

  <section class="column col-left sandwiches" style="top:738px">
    <h2 class="section-head">sandwiches</h2>
    <p class="section-note">(Served with french fries or garden salad)</p>
    <div class="rule"><span class="ornament" role="img" aria-label="Leaf ornament"></span></div>
    <ul class="menu-list" style="margin-top:4px">
      <li class="item" style="height:26px"><div class="item-name">Beef or Chicken Shawerma</div><span class="item-price">00</span></li>
      <li class="item" style="height:26px"><div class="item-name">Grilled Kofta</div><span class="item-price">00</span></li>
      <li class="item" style="height:39px"><div class="item-name">Greek Lamb Gyro</div><div class="item-desc">in pita bread with Tzatziki</div><span class="item-price">00</span></li>
      <li class="item"><div class="item-name">Club Sandwich</div><div class="item-desc">with smoked beef, turkey, egg</div><span class="item-price">00</span></li>
    </ul>
  </section>

  <section class="column col-left pizza-pasta" style="top:924px">
    <h2 class="section-head">pizza &amp; pasta</h2>
    <div class="rule"><span class="ornament" role="img" aria-label="Leaf ornament"></span></div>
    <ul class="menu-list" style="margin-top:2px">
      <li class="item" style="height:62px">
        <div class="item-name">Pizza Margarita <span style="text-transform:none">(Choose your toppings)</span></div>
        <span class="item-price">00</span>
        <div class="sub-option"><span class="bullet"></span>Bell Peppers, Olives, Tomato, Onion<span class="item-price">00</span></div>
        <div class="sub-option"><span class="bullet"></span>Mushroom, Chicken, Tuna, Pepperoni<span class="item-price">00</span></div>
        <div class="sub-option"><span class="bullet"></span>Smoked Salmon, Shrimps<span class="item-price">00</span></div>
      </li>
      <li class="item" style="height:65px">
        <div class="item-name">Create Your Own Pasta</div>
        <span class="item-price">00</span>
        <div class="sub-option">TYPE &nbsp;&nbsp;&nbsp;&nbsp;&nbsp;&nbsp;: Spaghetti, Tagliatelle, Penne</div>
        <div class="sub-option">SAUCES : Napolitana, Bolognese, Alfredo</div>
        <div class="sub-option">(Choose your toppings)</div>
      </li>
      <li class="item"><div class="item-name">Lasagna</div><span class="item-price">00</span></li>
    </ul>
  </section>

  <!-- Right column -->
  <section class="column col-right soups" style="top:200px">
    <h2 class="section-head">soups</h2>
    <div class="rule"><span class="ornament" role="img" aria-label="Leaf ornament"></span></div>
    <ul class="menu-list" style="margin-top:2px">
      <li class="item"><div class="item-name">Tomato Basil</div><div class="item-desc">Simmered tomato soup finished with<br>fresh basil and cream</div><span class="item-price">00</span></li>
      <li class="item"><div class="item-name">Chicken Cream</div><div class="item-desc">Chicken broth with roasted chicken cubes,<br>pine nuts, and cream</div><span class="item-price">00</span></li>
      <li class="item"><div class="item-name">Moroccan Harira</div><div class="item-desc">Vegetable broth with fresh tomato,<br>chickpeas, lentil, cilantro, and diced lamb</div><span class="item-price">00</span></li>
    </ul>
  </section>

  <section class="column col-right salads" style="top:392px">
    <h2 class="section-head">salads</h2>
    <div class="rule"><span class="ornament" role="img" aria-label="Leaf ornament"></span></div>
    <ul class="menu-list" style="margin-top:4px">
      <li class="item"><div class="item-name">Caprese</div><div class="item-desc">Buffalo mozzarella and sliced tomato<br>with a balsamic vinaigrette</div><span class="item-price">00</span></li>
      <li class="item"><div class="item-name">Rocket Apple</div><div class="item-desc">Rocket leaves with gorgonzola, croutons,<br>and strawberry vinaigrette</div><span class="item-price">00</span></li>
      <li class="item"><div class="item-name">French Riviera Nicoise</div><div class="item-desc">Lettuce, egg, tomato, tuna, olives, onion,<br>celery, radish, bell pepper in a French vinaigrette</div><span class="item-price">00</span></li>
      <li class="item"><div class="item-name">Folle</div><div class="item-desc">Mixed greens with crab sticks, mushroom,<br>corn, cherry tomato in a mango vinaigrette</div><span class="item-price">00</span></li>
    </ul>
  </section>

  <!-- Main courses panel -->
  <section class="mains-panel">
    <div class="mains-inner"></div>
    <h2 class="mains-head">main courses</h2>
    <div class="mains-rule"></div>
    <span class="mains-ornament" role="img" aria-label="Leaf ornament"></span>
    <ul class="mains-list">
      <li class="main-item" style="height:74px"><div class="item-name">Veal Parmeggiana</div><div class="item-desc">Breaded veal escalope topped with<br>melted cheese and tomato sauce<br>served with Spaghetti</div><span class="item-price">00</span></li>
      <li class="main-item" style="height:61px"><div class="item-name">Chicken a la Francaise</div><div class="item-desc">Pan fried chicken breast in a mushroom<br>cream sauce with vegetables white rice</div><span class="item-price">00</span></li>
      <li class="main-item" style="height:65px"><div class="item-name">Grilled Salmon</div><div class="item-desc">Salmon steak charcoal grilled with avocado<br>tomato relish and creamy mushroom risotto</div><span class="item-price">00</span></li>
      <li class="main-item" style="height:61px"><div class="item-name">Moroccan Chicken</div><div class="item-desc">Chicken cubes simmered with spices<br>and olives served with tomato rice</div><span class="item-price">00</span></li>
      <li class="main-item" style="height:65px"><div class="item-name">Filet</div><div class="item-desc">Tender filet grilled to your liking served with<br>mashed potato and creamed spinach</div><span class="item-price">00</span></li>
      <li class="main-item"><div class="item-name">Choice of Sauces</div>
        <div class="sauce">Brown Mushroom</div>
        <div class="sauce">Green Peppercorn</div>
        <div class="sauce">Gorgonzola</div>
      </li>
    </ul>
  </section>

  <div class="olive-art" role="img" aria-label="Illustration of an olive branch"></div>

  <div class="price-badge"><p>PRICES ARE SUBJECT TO 12% SERVICE CHARGE &amp; 10% SALES TAX</p></div>
</body>
</html>
```